Business Card Design Project

I am a Chiropractor that is looking for a new business card.  Our logo was slightly changed lately, therefore need a new, more professional look.
We are a modern, non-stuffy chiropractic office.  Want a contemporary look that will let people know this is not your typical doctors office.  Our logo is red, and contains the name of our business: realign.  The u in the logo is green, stressing the most important part of our business: "u"

Target Market(s)
moderate to upper income bracket, family friendly
www.realignspine-example.com
Gordon Pell
Family Chiropractor
314 Hollis Rd
Larkfield, ZX 78999
512.555.0147 phone
512.555.0148 fax
Industry/Entity Type
Business
Requirements
Must have
- www.realignspine-example.com
Gordon Pell
Family Chiropractor
314 Hollis Rd
Larkfield, ZX 78999
512.555.0147 phone
512.555.0148 fax

```html
<!DOCTYPE html>
<html lang="en">
<head>
<meta charset="utf-8">
<title>realign business card</title>
<link rel="stylesheet" href="https://fonts.googleapis.com/css2?family=Open+Sans:wght@300;400;800&display=swap">
<style>
  :root {
    --red: #e8463e;
    --green: #5bb134;
    --grey: #a8a8a8;
    --white: #ffffff;
    --backdrop: #e9e7e4;
    --card-w: 640px;
    --card-h: 366px;
  }
  * { box-sizing: border-box; margin: 0; padding: 0; }
  html, body {
    width: 1200px; height: 921px; overflow: hidden;
    background: var(--backdrop);
    font-family: "Open Sans", Arial, sans-serif;
  }
  .canvas { position: relative; width: 1200px; height: 921px; }
  .card {
    position: absolute; left: 280px;
    width: var(--card-w); height: var(--card-h);
    background: var(--white);
    box-shadow: 0 6px 18px rgba(0,0,0,.18);
    overflow: hidden;
  }
  /* Contact side */
  .card--contact { top: 64px; }
  .name-band {
    position: absolute; left: 20px; top: 40%;
    width: 47%; height: 22%;
    background: var(--red);
    padding: 18px 0 0 28px;
  }
  .name {
    color: var(--green); font-weight: 800; font-size: 27px; line-height: 1.05;
  }
  .title { color: #d9d9d9; font-size: 12.5px; margin-top: 2px; }
  .details {
    position: absolute; left: 59%; top: 34%;
    font-size: 13.5px; line-height: 19px;
  }
  .contact { list-style: none; }
  .contact li { display: flex; align-items: center; color: var(--red); }
  .contact .icon {
    display: inline-flex; align-items: center; justify-content: center;
    width: 12px; height: 12px; margin-right: 7px;
    background: var(--green); color: var(--white);
    font-size: 9px; font-weight: 800; border-radius: 2px;
  }
  .address { color: var(--green); font-style: normal; margin-top: 4px; }
  /* Brand side */
  .card--brand { top: 490px; }
  .band { position: absolute; left: 0; width: 100%; background: var(--red); }
  .band--top { top: 0; height: 13%; }
  .band--bottom { bottom: 0; height: 21%; }
  .brand {
    position: absolute; left: 0; right: 0; top: 13%; bottom: 21%;
    display: flex; align-items: center; justify-content: center; gap: 18px;
  }
  .brand-dot { width: 26px; height: 26px; border-radius: 50%; background: var(--red); }
  .brand-name {
    color: var(--red); font-weight: 300; font-size: 96px; letter-spacing: 4px; line-height: 1;
  }
</style>
</head>
<body>
<main class="canvas">
  <section class="card card--contact" aria-label="Card back with contact details">
    <div class="name-band">
      <h1 class="name">Gordon Pell</h1>
      <p class="title">Family Chiropractor</p>
    </div>
    <div class="details">
      <ul class="contact">
        <li><span class="icon">p</span>512.555.0147</li>
        <li><span class="icon">f</span>512.555.0148</li>
        <li><span class="icon">w</span>www.realignspine-example.com</li>
      </ul>
      <address class="address">314 Hollis Rd<br>Larkfield, ZX 78999</address>
    </div>
  </section>

  <section class="card card--brand" aria-label="Card front with brand name">
    <div class="band band--top"></div>
    <div class="brand">
      <span class="brand-dot"></span>
      <span class="brand-name">realign</span>
    </div>
    <div class="band band--bottom"></div>
  </section>
</main>
</body>
</html>
```